Book cover for a book on tactics, habits and directives learned from world class performers

The Quiet Ledger book is the first in a series of four books filled with proven tactics, habits and directives (i.e., what to do) that young, ambitious working professionals should be doing to make their life better. The first book is on foundational or keystone habits - that is, the habits that will help everyone upgrade their life and enable other great habits in their life (things such as waking up early in the morning or exercising)

The goal of the book is to stand out on the Brimvale platform as a small thumbnail, as well as a 5 x 8 book.

The imagery should make the viewer feel that the book (and the author) are the authority in habits and developing habits.

The reader should feel that they must have this book if they know they should be developing successful habits but do not want to comb through hundreds of books just to find the one tactic or habit that they should be doing. It's important that the book "pops off the shelf" and catches the eye quickly.

The most important part of the design is that it sells, not that it looks well-designed. I am open to any image or illustration you choose though please consider the nice have I have listed below. Here are a few words that come to mind when thinking of my book: growth, self development, leadership, success, freedom, passion, motivation, young professional, accomplished, experience.

I like a bold color palette. I like bold titles that you know right away what the title is and what it is about, not too busy and with simple color schemes. 2 - 3 colors.

Books with covers I like:
- Lamp Orchard by Norris Pellaquin
- Under The Copper Tide by Gordon Pruitt
- The Velvet Compass by Edgar Fulbright

Target Market(s)

- Young 20 - 40 year old ambitious working professionals interested in self development and listen to podcasts of Ned Caplow, Rufus Denholme
- Just starting out management consultants

Colors

Designer to choose colors to be used in the design.

Requirements
Must have
• 'Quiet Ledger' title - first and foremost
• Author name - Lu Qiao - probably on the bottom or somewhere
• Bold colour / colours or a graphic that is eye catching (and makes it different from other habits books on Brimvale)
Nice to have
• Would like to have some sort of visual, colour or theme that can run through the four books - would be great to have a cover design that can be simply changed to depict the second, third or fourth book in the series - maybe the graphic or visual can be changed with some colours, etc. but with the overall feel looking similar so that people can see that it's part of the same book series

```html
<!DOCTYPE html>
<html lang="en">
<head>
<meta charset="utf-8">
<title>Quiet Ledger — Lu Qiao</title>
<link rel="stylesheet" href="https://fonts.googleapis.com/css2?family=Bebas+Neue&family=Oswald:wght@400;600&display=swap">
<style>
  :root {
    --paper: #ffffff;
    --ink: #141414;
    --ink-soft: #3a3a3a;
    --signal-red: #e3202b;
    --deep-red: #c8141f;
    --blush: #f6a9c4;
    --pale-pink: #fbd9e6;
  }
  html, body {
    margin: 0;
    padding: 0;
    width: 800px;
    height: 1200px;
    overflow: hidden;
    background: var(--paper);
  }
  .cover {
    position: relative;
    width: 800px;
    height: 1200px;
    background: var(--paper);
    overflow: hidden;
  }
  .series-tagline {
    position: absolute;
    top: 28px;
    left: 0;
    width: 100%;
    margin: 0;
    text-align: center;
    font-family: "Oswald", sans-serif;
    font-weight: 400;
    font-size: 17px;
    letter-spacing: 0.22em;
    color: var(--ink-soft);
  }
  .hero-artwork {
    position: absolute;
    left: 150px;
    top: 66px;
    width: 520px;
    height: 790px;
    border-radius: 46% 46% 40% 40% / 30% 30% 44% 44%;
    background:
      radial-gradient(ellipse 55% 45% at 50% 62%, var(--signal-red) 0%, var(--deep-red) 45%, rgba(227,32,43,0) 80%),
      radial-gradient(ellipse 70% 60% at 50% 35%, var(--blush) 0%, var(--pale-pink) 55%, rgba(251,217,230,0) 100%);
  }
  .author {
    position: absolute;
    right: 85px;
    top: 846px;
    margin: 0;
    font-family: "Oswald", sans-serif;
    font-weight: 400;
    font-size: 32px;
    line-height: 1.2;
    letter-spacing: 0.14em;
    color: var(--ink);
  }
  .title {
    position: absolute;
    left: 0;
    top: 903px;
    width: 100%;
    margin: 0;
    text-align: center;
    font-family: "Bebas Neue", sans-serif;
    font-weight: 400;
    font-size: 152px;
    line-height: 1;
    letter-spacing: 0.01em;
    color: var(--ink);
  }
  .volume-label {
    position: absolute;
    left: 200px;
    top: 1052px;
    margin: 0;
    font-family: "Oswald", sans-serif;
    font-weight: 600;
    font-size: 36px;
    line-height: 1.2;
    letter-spacing: 0.02em;
    color: var(--signal-red);
  }
  .volume-marker {
    position: absolute;
    left: 468px;
    top: 1050px;
    width: 60px;
    height: 60px;
    background: var(--ink);
  }
</style>
</head>
<body>
  <main class="cover">
    <p class="series-tagline">HABITS TO PROMOTE SUCCESS AND WELLBEING</p>

    <div class="hero-artwork" role="img" aria-label="Illustration of a calm human head built from red and pink tiles, with an open doorway at the crown"></div>

    <p class="author">LU QIAO</p>
    <h1 class="title">QUIET LEDGER</h1>
    <p class="volume-label">FOUNDATIONAL</p>
    <div class="volume-marker" aria-hidden="true"></div>
  </main>
</body>
</html>
```